Physiotherapiepraxis braucht Druckvorlage für Werbeanzeige
Zielgruppe
Dienstleistung im Gesundheitswesen als Physiotherapiepraxis.
Krankengymnastik, auch im häuslichen Bereich oder im Altersheim, und Massage sowie Wellnessanwendungen.
Zielgruppe sind primär Erwachsene, eingeschränkt auch Kinder.
Aufgabenstellung
Ich möchte eine Druckvorlage für eine Werbeanzeige, die ich immer mal wieder in verschiedenen Festschriften im dörflichen Bereich oder in einer regionalen Zeitschrift veröffentlichen kann.
Die Anzeige soll das Logo enthalten und die Anschrift der Praxis sowie die Telefonnummer und Adresse der Homepage.

```html
<!DOCTYPE html>
<html lang="de">
<head>
<meta charset="utf-8">
<title>Anzeigen Physiotherapie Marlene Hoppe</title>
<link href="https://fonts.googleapis.com/css2?family=Source+Sans+3:wght@400;700&display=swap" rel="stylesheet">
<style>
  :root{
    --gold:#d4b823;
    --green:#007a3b;
    --grey:#555556;
    --heading:#4a4a4a;
    --paper:#ffffff;
    --name-colour:#007a3b;
  }
  *{box-sizing:border-box;margin:0;padding:0}
  html,body{width:1200px;height:846px;overflow:hidden;background:var(--paper)}
  body{position:relative;font-family:"Source Sans 3",sans-serif}

  .section-title{
    position:absolute;font-weight:400;font-size:21px;color:var(--heading);
  }
  .section-title--single{left:142px;top:41px}
  .section-title--double{left:344px;top:382px}

  .ad{position:absolute;background:var(--brand);color:var(--paper)}
  .ad--gold{--brand:var(--gold)}
  .ad--green{--brand:var(--green)}
  .ad--grey{--brand:var(--grey);--name-colour:var(--grey)}

  .ad__info{position:absolute;font-size:14.5px;line-height:18px}
  .ad__info p{margin:0}
  .ad__info .strong{font-weight:700}
  .ad__info .gap{margin-top:5px}

  .ad__logo{
    position:absolute;background:var(--paper);
    display:flex;align-items:center;justify-content:center;gap:8px;
  }
  .logo-dot{width:11px;height:11px;border-radius:50%;background:var(--name-colour);flex:none}
  .logo-name{font-size:21px;font-weight:400;letter-spacing:2px;color:var(--name-colour)}

  /* 1-spaltig */
  .ad--single{width:257px;height:257px;top:81px}
  .ad--single .ad__info{left:15px;top:10px}
  .ad--single .ad__logo{left:2px;right:2px;top:137px;bottom:9px}

  /* 2-spaltig */
  .ad--double{width:514px;height:113px;left:344px}
  .ad--double .ad__info{left:13px;top:10px}
  .ad--double .ad__logo{left:257px;right:1px;top:6px;bottom:1px}
</style>
</head>
<body>

<h2 class="section-title section-title--single">Anzeigen 1-spaltig, 45 mm breit</h2>

<article class="ad ad--single ad--gold" style="left:142px">
  <div class="ad__info">
    <p class="strong">Praxis für Physiotherapie<br>Marlene Hoppe</p>
    <p class="gap">Lindenweg 7<br>21487 Wiesendorf</p>
    <p class="gap">Tel. 04155 - 48 27 19</p>
    <p class="strong">www.physio-wiesendorf.de</p>
  </div>
  <div class="ad__logo"><span class="logo-dot"></span><span class="logo-name">Marlene Hoppe</span></div>
</article>

<article class="ad ad--single ad--green" style="left:471px">
  <div class="ad__info">
    <p class="strong">Praxis für Physiotherapie<br>Marlene Hoppe</p>
    <p class="gap">Lindenweg 7<br>21487 Wiesendorf</p>
    <p class="gap">Tel. 04155 - 48 27 19</p>
    <p class="strong">www.physio-wiesendorf.de</p>
  </div>
  <div class="ad__logo"><span class="logo-dot"></span><span class="logo-name">Marlene Hoppe</span></div>
</article>

<article class="ad ad--single ad--grey" style="left:800px">
  <div class="ad__info">
    <p class="strong">Praxis für Physiotherapie<br>Marlene Hoppe</p>
    <p class="gap">Lindenweg 7<br>21487 Wiesendorf</p>
    <p class="gap">Tel. 04155 - 48 27 19</p>
    <p class="strong">www.physio-wiesendorf.de</p>
  </div>
  <div class="ad__logo"><span class="logo-dot"></span><span class="logo-name">Marlene Hoppe</span></div>
</article>

<h2 class="section-title section-title--double">Anzeigen 2-spaltig, 90 mm breit</h2>

<article class="ad ad--double ad--gold" style="top:422px">
  <div class="ad__info">
    <p class="strong">Praxis für Physiotherapie<br>Marlene Hoppe</p>
    <p class="gap">Lindenweg 7, 21487 Wiesendorf</p>
    <p class="gap">Tel. 04155 - 48 27 19</p>
    <p class="strong">www.physio-wiesendorf.de</p>
  </div>
  <div class="ad__logo"><span class="logo-dot"></span><span class="logo-name">Marlene Hoppe</span></div>
</article>

<article class="ad ad--double ad--green" style="top:557px">
  <div class="ad__info">
    <p class="strong">Praxis für Physiotherapie<br>Marlene Hoppe</p>
    <p class="gap">Lindenweg 7, 21487 Wiesendorf</p>
    <p class="gap">Tel. 04155 - 48 27 19</p>
    <p class="strong">www.physio-wiesendorf.de</p>
  </div>
  <div class="ad__logo"><span class="logo-dot"></span><span class="logo-name">Marlene Hoppe</span></div>
</article>

<article class="ad ad--double ad--grey" style="top:693px">
  <div class="ad__info">
    <p class="strong">Praxis für Physiotherapie<br>Marlene Hoppe</p>
    <p class="gap">Lindenweg 7, 21487 Wiesendorf</p>
    <p class="gap">Tel. 04155 - 48 27 19</p>
    <p class="strong">www.physio-wiesendorf.de</p>
  </div>
  <div class="ad__logo"><span class="logo-dot"></span><span class="logo-name">Marlene Hoppe</span></div>
</article>

</body>
</html>
```